Business Card Design

I am starting my therapy private practice. I will be an in home therapist, so I go into family's homes instead of using an office to do family/marriage therapy. Therefore, I do not have an office address. I am looking for something in the black, red, gray, and blue color scheme that appeals to both families, couples and teenagers.

Industry/Entity Type

Business

Contact Information for Business Card

Lena Brightwell, MS, MFT Intern
Marriage and Family Therapy
In Home Therapist
617-482-5190
Lena@LenaBrightwell-example.com

```html
<!DOCTYPE html>
<html lang="en">
<head>
<meta charset="utf-8">
<title>Lena Brightwell – Business Card</title>
<link rel="stylesheet" href="https://fonts.googleapis.com/css2?family=Open+Sans:wght@400;600&display=swap">
<style>
  :root {
    --page-bg: #ecebe8;
    --card-white: #ffffff;
    --brand-blue: #3a4ea6;
    --brand-red: #d32833;
    --text-gray: #6b6b6b;
    --text-white: #ffffff;
  }
  * { margin: 0; padding: 0; box-sizing: border-box; }
  html, body {
    width: 1200px;
    height: 1023px;
    overflow: hidden;
    background: var(--page-bg);
    font-family: "Open Sans", Arial, sans-serif;
  }
  .card {
    position: absolute;
    left: 100px;
    top: 226px;
    width: 1000px;
    height: 571px;
    display: flex;
    box-shadow: 0 14px 40px rgba(0,0,0,0.18);
    overflow: hidden;
  }
  .card__identity {
    position: relative;
    width: 48%;
    background: var(--card-white);
    display: flex;
    flex-direction: column;
    justify-content: center;
    padding-left: 64px;
  }
  .brand {
    display: flex;
    align-items: center;
    gap: 18px;
  }
  .brand__dot {
    width: 46px;
    height: 46px;
    border-radius: 50%;
    background: var(--brand-blue);
    flex: none;
  }
  .brand__name {
    font-size: 40px;
    font-weight: 400;
    color: var(--brand-blue);
    letter-spacing: 0.5px;
  }
  .brand__tagline {
    margin-top: 14px;
    margin-left: 64px;
    font-size: 17px;
    line-height: 1.45;
    color: var(--text-gray);
  }
  .card__details {
    width: 52%;
    display: flex;
    flex-direction: column;
  }
  .details__name-band {
    flex: 0 0 46%;
    background: var(--brand-blue);
    color: var(--text-white);
    padding: 58px 48px 0 52px;
  }
  .details__name {
    font-size: 34px;
    font-weight: 400;
  }
  .details__title {
    margin-top: 8px;
    font-size: 20px;
    line-height: 1.4;
  }
  .details__contact-band {
    flex: 1;
    background: var(--brand-red);
    color: var(--text-white);
    padding: 54px 40px 0 0;
    position: relative;
  }
  .contact {
    display: flex;
    align-items: center;
    gap: 22px;
    margin-left: -24px;
    margin-bottom: 34px;
    font-size: 21px;
  }
  .contact__icon {
    width: 48px;
    height: 48px;
    border-radius: 50%;
    background: var(--card-white);
    border: 3px solid var(--brand-red);
    display: flex;
    align-items: center;
    justify-content: center;
    flex: none;
  }
  .contact__icon svg { width: 22px; height: 22px; }
</style>
</head>
<body>
  <section class="card">
    <div class="card__identity">
      <div class="brand">
        <span class="brand__dot"></span>
        <span class="brand__name">Lena Brightwell</span>
      </div>
      <p class="brand__tagline">MS, MFT Intern Marriage and<br>Family Therapy In Home Therapist</p>
    </div>
    <div class="card__details">
      <div class="details__name-band">
        <h1 class="details__name">Lena Brightwell</h1>
        <p class="details__title">MS, MFT Intern Marriage and<br>Family Therapy In Home Therapist</p>
      </div>
      <div class="details__contact-band">
        <div class="contact">
          <span class="contact__icon">
            <svg viewBox="0 0 24 24" aria-hidden="true"><path fill="#d32833" d="M6.6 10.8a15.1 15.1 0 0 0 6.6 6.6l2.2-2.2a1 1 0 0 1 1-.25 11.4 11.4 0 0 0 3.6.57 1 1 0 0 1 1 1V20a1 1 0 0 1-1 1A17 17 0 0 1 3 4a1 1 0 0 1 1-1h3.5a1 1 0 0 1 1 1c0 1.25.2 2.46.57 3.6a1 1 0 0 1-.25 1z"/></svg>
          </span>
          <span class="contact__text">617-482-5190</span>
        </div>
        <div class="contact">
          <span class="contact__icon">
            <svg viewBox="0 0 24 24" aria-hidden="true"><text x="12" y="18" text-anchor="middle" font-family="Open Sans, Arial, sans-serif" font-size="18" font-weight="600" fill="#3a4ea6">@</text></svg>
          </span>
          <span class="contact__text">Lena@LenaBrightwell-example.com</span>
        </div>
      </div>
    </div>
  </section>
</body>
</html>
```